Website design for a high-end equestrian business

Design a website to replace current one. Clean, simple, elegant design. I run a business training show jumping riders and horses, as well as buying and selling high quality horses. I run my business from a beautiful yard in Co. Kildare, Ireland. Reference to Ireland and quality sport horses is important in the website.

Current website is www.sorchapelletrow.com. One page in particular that I need is a "Sport Horses" page as well as a "References" page. Layout for each to be similar to this one - https://www.brimlowfields.net/en/sporthorses

Another website I like the feel of is www.velarocourse.com
Colour theme to be charcoal grey with elements of lighter grey and cream, as per logo. Charcoal grey to be somewhat transparent, otherwise it takes over too much. Cream colour is also to be subtle and not too beige.

Please note that Pelletrow is one word.

Please note there are new photographs with which to work if desired.

Sick

Target Market(s)

Upmarket clients seeking high quality coaching services and high quality show jumping horses

Number of Pages Required

2 page

Font styles to use
Serif
Sans Serif

Colors

Designer to choose only greyscale colors for use in the design.

Requirements
Must have
• A clean, simple, elegant look to the final design. OVerall theme colours must be subtle and include charcoal grey, light grey and cream. A design that will work well for mobile also. Please include only photographs provided or on the old website.
Nice to have
• artistically integrated photographs. use of the logo.
Should not have
• Anything fussy.

```html
<!DOCTYPE html>
<html lang="en">
<head>
<meta charset="utf-8">
<title>Sorcha Pelletrow – Show Jumping</title>
<link rel="stylesheet" href="https://fonts.googleapis.com/css2?family=Roboto:wght@300;400;700&family=Lato:wght@400;700&display=swap">
<style>
:root{
  --charcoal:#2b2b2b;
  --charcoal-mid:#333333;
  --slate:#444444;
  --gold:#b9a46c;
  --white:#ffffff;
  --muted:#d5d5d5;
  --line:#8a8a8a;
}
*{margin:0;padding:0;box-sizing:border-box}
html,body{width:1200px;height:3349px;overflow:hidden;background:var(--charcoal)}
body{position:relative;font-family:"Lato",sans-serif;color:var(--white)}
.abs{position:absolute}
.heading{font-family:"Roboto",sans-serif;font-weight:300;text-transform:uppercase;text-align:center;width:1200px;left:0}
.rule{position:absolute;height:3px;background:var(--white);width:66px;left:567px}

/* header */
.site-header{position:absolute;top:0;left:0;width:1200px;height:100px;background:var(--charcoal)}
.brand{position:absolute;font-family:"Lato",sans-serif;font-weight:400;color:var(--gold);letter-spacing:1px}
.site-header .brand{left:162px;top:30px;font-size:30px}
.nav a{position:absolute;font-family:"Roboto",sans-serif;font-size:15px;color:var(--muted);text-decoration:none;text-transform:uppercase;white-space:nowrap}
.site-header .nav a{top:42px}
.nav a.active{border:2px solid var(--gold);color:var(--gold);font-weight:700;padding:8px 18px;top:34px}

/* hero */
.hero{position:absolute;top:100px;left:0;width:1200px;height:572px;background:linear-gradient(180deg,#6f6a58 0%,#8a6a4a 40%,#6b7d3e 78%,#5e8a37 100%)}
.hero-caption{position:absolute;left:308px;top:225px;width:560px;height:173px;background:rgba(70,70,70,.82);text-align:center;font-family:"Roboto",sans-serif;font-weight:300;text-transform:uppercase}
.hero-caption .pre{font-size:36px;margin-top:30px}
.hero-caption .name{font-size:52px;margin-top:2px}
.dots span{position:absolute;top:527px;width:18px;height:18px;border:2px solid var(--white);border-radius:50%}
.dots span.on{background:var(--white)}

/* welcome */
.welcome{position:absolute;top:672px;left:0;width:1200px;height:433px;background:var(--charcoal-mid)}
.welcome p{position:absolute;left:210px;width:780px;top:160px;text-align:center;font-size:18px;line-height:27px;color:var(--muted)}
.btn{position:absolute;border:2px solid var(--gold);color:var(--gold);font-family:"Roboto",sans-serif;font-weight:700;font-size:16px;text-align:center;text-transform:uppercase}

/* horses */
.horse{position:absolute;top:1221px;width:295px;height:268px}
.horse .photo{height:214px}
.horse .label{height:54px;background:var(--charcoal);font-family:"Roboto",sans-serif;font-weight:700;font-size:21px;text-align:center;line-height:54px;text-transform:uppercase}

/* services */
.service{position:absolute;top:1737px;width:219px;height:233px;border:2px solid var(--line);text-align:center}
.service .icon{position:absolute;left:67px;top:-44px;width:84px;height:84px;border-radius:50%;background:var(--gold)}
.service h3{font-family:"Roboto",sans-serif;font-weight:700;font-size:17px;margin-top:62px;text-transform:uppercase}
.service p{font-size:12px;line-height:19px;color:var(--muted);padding:0 12px;margin-top:12px}
.service .more{position:absolute;left:89px;bottom:-22px;width:40px;height:40px;border-radius:50%;background:var(--charcoal)}

/* gallery */
.thumb{position:absolute;top:2220px;width:206px;height:189px;border:3px solid var(--white)}

/* news */
.news-meta{font-size:13px;color:var(--muted)}
.news-title{font-family:"Lato",sans-serif;font-weight:700;font-size:18px;line-height:24px;text-transform:uppercase}
.news-more{font-size:16px;color:var(--gold)}
.news-item{position:absolute;left:630px;width:415px;height:118px}
.news-item .photo{position:absolute;left:0;top:0;width:128px;height:117px}
.news-item .txt{position:absolute;left:156px;top:10px;width:270px}
.news-item .txt .news-title{margin-top:6px;font-size:17px;line-height:23px}
.news-item .txt .news-more{display:block;margin-top:12px}
.sep{position:absolute;left:629px;width:416px;height:1px;background:var(--line)}

/* footer */
.site-footer{position:absolute;top:3198px;left:0;width:1200px;height:151px;background:var(--charcoal)}
.site-footer .brand{left:136px;top:36px;font-size:28px}
.site-footer .nav a{top:53px;font-size:14px}
.copy{position:absolute;left:348px;top:83px;font-size:12px;color:var(--muted)}
.social{position:absolute;top:56px;width:16px;height:16px;border-radius:50%;border:2px solid var(--muted)}
</style>
</head>
<body>

<header class="site-header">
  <div class="brand">Pelletrow</div>
  <nav class="nav">
    <a class="active" style="left:403px">About</a>
    <a style="left:519px">Horses</a>
    <a style="left:612px">Sponsors</a>
    <a style="left:728px">Facilities &amp; Services</a>
    <a style="left:922px">Gallery</a>
    <a style="left:1022px">Contact</a>
  </nav>
</header>

<section class="hero" role="img" aria-label="Rider on a chestnut horse clearing a fence in front of a crowded grandstand">
  <div class="hero-caption">
    <div class="pre">Welcome to</div>
    <div class="name">Sorcha Pelletrow</div>
  </div>
  <div class="dots"><span style="left:569px"></span><span class="on" style="left:598px"></span><span style="left:628px"></span></div>
</section>

<section class="welcome">
  <h2 class="heading abs" style="top:84px;font-size:36px">Welcome to SP</h2>
  <div class="rule" style="top:136px"></div>
  <p>From Ballyrane in Co. Kildare, Sorcha is 31 years old and has been passionate about horses since she was a child. Over the years she has achieved many successes with a variety of equine partners, from Pony National Champion two years running on Silver Marsh</p>
  <div class="btn" style="left:510px;top:274px;width:179px;height:52px;line-height:48px">Learn More</div>
</section>

<svg class="abs" style="top:1080px;left:0" width="1200" height="520" viewBox="0 0 1200 520" aria-hidden="true">
  <rect width="1200" height="520" fill="#444444"/>
  <rect width="1200" height="25" fill="#333333"/>
  <path d="M0 25 C300 0 700 40 1200 130 L1200 500 C900 520 500 480 0 410 Z" fill="#b9a46c"/>
</svg>

<h2 class="heading abs" style="top:1150px;font-size:31px;color:var(--charcoal)">Current Horses</h2>
<div class="horse" style="left:135px"><div class="photo" role="img" aria-label="Rider beside her bay horse in a bridle" style="background:linear-gradient(135deg,#6b4a30,#3a3a30 60%,#8a8a80)"></div><div class="label">Horse Title</div></div>
<div class="horse" style="left:454px"><div class="photo" role="img" aria-label="Bay horse standing beside its rider" style="background:linear-gradient(135deg,#3c8a3a,#4a3022 55%,#d8d8d8)"></div><div class="label">Horse Title</div></div>
<div class="horse" style="left:768px"><div class="photo" role="img" aria-label="Chestnut horse jumping a fence under blue sky" style="background:linear-gradient(180deg,#6f9fd0,#8a5a34 60%,#c8c8c8)"></div><div class="label">Horse Title</div></div>

<h2 class="heading abs" style="top:1636px;font-size:31px">Facilities &amp; Services</h2>
<div class="rule" style="top:1682px"></div>

<div class="service" style="left:144px"><div class="icon"></div><h3>Consultancy</h3><p>Sorcha has completed a variety of consulting work within the equestrian industry, from valuations</p><div class="more"></div></div>
<div class="service" style="left:377px"><div class="icon"></div><h3>Schooling</h3><p>In more recent years, riders, owners and producers have begun to recognise the importance and value of correct</p><div class="more"></div></div>
<div class="service" style="left:610px"><div class="icon"></div><h3>Coaching</h3><p>Sorcha is an accomplished coach with the internationally-recognised RCA Level 2 qualification. Having worked with riders from</p><div class="more"></div></div>
<div class="service" style="left:842px"><div class="icon"></div><h3>Facilities</h3><p>The facilities at X Stables are top-class. Two American barns contain a total of 15 luxury loose boxes</p><div class="more"></div></div>

<svg class="abs" style="top:1930px;left:0;pointer-events:none" width="1200" height="70" aria-hidden="true">
  <g fill="none" stroke="#ffffff" stroke-width="2">
    <path d="M239 30 l8 8 l8 -8"/><path d="M472 30 l8 8 l8 -8"/><path d="M705 30 l8 8 l8 -8"/><path d="M937 30 l8 8 l8 -8"/>
  </g>
</svg>

<svg class="abs" style="top:2080px;left:0" width="1200" height="470" viewBox="0 0 1200 470" aria-hidden="true">
  <rect width="1200" height="470" fill="#444444"/>
  <path d="M0 0 H1200 V455 C900 430 400 420 0 350 Z" fill="#262626"/>
</svg>

<h2 class="heading abs" style="top:2135px;font-size:36px">Our Gallery</h2>
<div class="rule" style="top:2185px"></div>
<div class="thumb" style="left:153px;background:linear-gradient(135deg,#2c4f8a,#c89c7a 50%,#1e3a6a)" role="img" aria-label="Smiling rider in a cap and blue jacket"></div>
<div class="thumb" style="left:387px;background:linear-gradient(180deg,#4e7a3a,#e0e0e0 55%,#c84a3a)" role="img" aria-label="Horse and rider jumping beside white show tents"></div>
<div class="thumb" style="left:618px;background:linear-gradient(180deg,#8a4a4a,#6a4a2e 50%,#c8892e)" role="img" aria-label="Horse jumping a wooden fence in a crowded arena"></div>
<div class="thumb" style="left:852px;background:linear-gradient(135deg,#6a7a8a,#1f3a24 55%,#3a3a3a)" role="img" aria-label="Rider in a green show jacket at the arena"></div>

<h2 class="heading abs" style="top:2585px;font-size:31px;left:-8px">Latest News</h2>
<div class="rule" style="top:2631px;left:560px"></div>

<div class="abs" style="left:160px;top:2662px;width:428px;height:241px;background:linear-gradient(180deg,#6a9a3a,#8a5a34 55%,#3e6a2a)" role="img" aria-label="Rider on a bay horse clearing a green fence"></div>
<div class="abs" style="left:170px;top:2932px;width:420px">
  <div class="news-meta">April 12, 2019 &nbsp;|&nbsp; No Comments</div>
  <div class="news-title" style="margin-top:10px">Mauris vel lacus vitae felis vestibulum volutpat etiam est nunc</div>
  <p style="font-size:13px;line-height:21px;color:var(--muted);margin-top:12px">Nunc tempus felis vitae urna Vivamus porttitor neque at volutpat rutrum purus nisi eleifend libero a tempus libero lectus</p>
  <div class="news-more" style="margin-top:12px">Learn More</div>
</div>

<div class="news-item" style="top:2662px"><div class="photo" role="img" aria-label="Black and white portrait of a rider" style="background:linear-gradient(135deg,#2a2a2a,#9a9a9a)"></div><div class="txt"><div class="news-meta">April 08, 2019 &nbsp;|&nbsp; No Comments</div><div class="news-title">Mauris vel lacus vitae felis vestibulum volutpat</div><span class="news-more">Learn More</span></div></div>
<div class="sep" style="top:2798px"></div>
<div class="news-item" style="top:2822px"><div class="photo" role="img" aria-label="Rider on a bay horse at a show" style="background:linear-gradient(180deg,#6a8a4a,#5a3a24)"></div><div class="txt"><div class="news-meta">April 06, 2019 &nbsp;|&nbsp; No Comments</div><div class="news-title">Fusce tellus sed metus augue convallis et</div><span class="news-more">Learn More</span></div></div>
<div class="sep" style="top:2961px"></div>
<div class="news-item" style="top:2983px"><div class="photo" role="img" aria-label="Close view of a rider over a jump" style="background:linear-gradient(135deg,#2e4a2e,#d8d8d8 50%,#6a3a24)"></div><div class="txt"><div class="news-meta">April 02, 2019 &nbsp;|&nbsp; No Comments</div><div class="news-title">Phasellus felis dolor scelerisque a tempus</div><span class="news-more">Learn More</span></div></div>

<footer class="site-footer">
  <div class="brand">Pelletrow</div>
  <nav class="nav">
    <a style="left:348px">About</a>
    <a style="left:425px">Horses</a>
    <a style="left:516px">Sponsors</a>
    <a style="left:627px">Facilities &amp; Services</a>
    <a style="left:815px">Gallery</a>
    <a style="left:910px">Contact</a>
  </nav>
  <div class="copy">© 2019 Company Name &nbsp;All right reserved</div>
  <span class="social" style="left:1008px" aria-label="Social profile"></span>
  <span class="social" style="left:1054px" aria-label="Social profile"></span>
  <span class="social" style="left:1101px" aria-label="Social profile"></span>
</footer>

</body>
</html>
```